Business Card Design Project - bel soravin group

dear Sirs

we need business card design for our group ( BEL Soravin Group ) , i have got the Logo design of our group from pixel harbor in previous , so all need details relating to our group i think available with you, as well as the the chosen logo design

we hope to provide us with business card logo that to be appropaite and satisfactory to us .

thanks

note : logo design of our group is attached .
Updates

Reason: please extend the deadline of my project for additional 15 days because i didn't received appropriate design for our gruop yet . kindly beaware that i have received 77 design till now , supossed to send me 200-250 design at least . thanks

Target Market(s)

contents
-

name : Korvan EL Mistrani

position : Operation Manager

Industry/Entity Type

Business

Requirements
Must have

• person name

group logo
Nice to have
• logo color matching with back background

```html
<!DOCTYPE html>
<html lang="en">
<head>
<meta charset="utf-8">
<title>BEL Soravin Group – Business Card</title>
<link rel="stylesheet" href="https://fonts.googleapis.com/css2?family=Open+Sans:wght@400;600&display=swap">
<style>
  :root {
    --page-bg: #e4e6e9;
    --brand-blue: #1f5fb0;
    --brand-blue-light: #4f8fd6;
    --brand-blue-dark: #164a8c;
    --silver-light: #f2f3f4;
    --silver-mid: #c6c9cc;
    --silver-dark: #7d8186;
    --paper-grey: #dcdddf;
    --accent-gold: #e0a21c;
    --text-white: #ffffff;
    --text-navy: #1b3f73;
  }
  * { box-sizing: border-box; margin: 0; padding: 0; }
  html, body { width: 1200px; height: 900px; overflow: hidden; }
  body {
    background: var(--page-bg);
    font-family: "Open Sans", Arial, sans-serif;
    display: flex;
    flex-direction: column;
    align-items: center;
    justify-content: center;
    gap: 44px;
  }
  .card {
    position: relative;
    width: 600px;
    height: 343px;
    overflow: hidden;
    box-shadow: 0 6px 18px rgba(0,0,0,0.18);
  }
  .silver-band {
    background: linear-gradient(180deg, var(--silver-dark) 0%, var(--silver-light) 45%, var(--silver-mid) 70%, var(--silver-light) 100%);
  }

  /* Front */
  .card-front { display: flex; flex-direction: column; background: var(--brand-blue); }
  .card-front .stripe { flex: none; }
  .stripe-pale { height: 58px; background: var(--paper-grey); }
  .stripe-silver { height: 46px; }
  .stripe-logo {
    height: 92px;
    background: var(--brand-blue);
    display: flex; align-items: center; justify-content: center;
  }
  .stripe-footer {
    height: 47px;
    background: var(--paper-grey);
    display: flex; align-items: center; justify-content: space-between;
    padding: 0 22px;
    font-size: 12px; color: var(--text-navy);
  }

  .brand-mark { display: flex; align-items: center; gap: 12px; }
  .brand-mark .brand-square {
    width: 22px; height: 22px; background: var(--accent-gold);
  }
  .brand-mark .brand-name {
    color: var(--text-white);
    font-weight: 600;
    letter-spacing: 1px;
  }
  .card-front .brand-name { font-size: 34px; }

  /* Back */
  .card-back {
    background: radial-gradient(ellipse at 35% 55%, var(--brand-blue-light) 0%, var(--brand-blue) 55%, var(--brand-blue-dark) 100%);
  }
  .back-top {
    position: absolute; left: 0; top: 0; width: 100%; height: 70px;
    display: flex; align-items: center; padding-left: 26px;
    border-bottom: 1px solid rgba(255,255,255,0.55);
  }
  .card-back .brand-name { font-size: 24px; }
  .back-body {
    position: absolute; left: 0; top: 70px; width: 100%; height: 203px;
    display: flex; align-items: center;
  }
  .person { flex: 1; padding-left: 60px; }
  .person-name { color: var(--text-white); font-size: 26px; font-weight: 400; }
  .person-role { color: var(--accent-gold); font-size: 17px; margin-top: 2px; }
  .contact-list {
    list-style: none;
    width: 230px; height: 140px;
    border-left: 1px solid rgba(255,255,255,0.75);
    padding-left: 18px;
    display: flex; flex-direction: column; justify-content: center; gap: 5px;
    color: var(--text-white); font-size: 13px;
    margin-right: 40px;
  }
  .back-footer {
    position: absolute; left: 0; bottom: 0; width: 100%; height: 70px;
    display: flex; align-items: flex-end; justify-content: space-between;
    padding: 0 24px 12px;
    color: var(--text-navy); font-size: 13px; font-weight: 600;
  }
  .back-footer .address { line-height: 1.35; }
  .back-edge {
    position: absolute; left: 0; bottom: 70px; width: 100%; height: 8px;
    background: var(--brand-blue-dark);
  }
</style>
</head>
<body>

  <section class="card card-front" aria-label="Business card front">
    <div class="stripe stripe-pale"></div>
    <div class="stripe stripe-silver silver-band"></div>
    <div class="stripe stripe-logo">
      <div class="brand-mark">
        <span class="brand-square"></span>
        <span class="brand-name">BEL SORAVIN GROUP</span>
      </div>
    </div>
    <div class="stripe stripe-silver silver-band"></div>
    <div class="stripe stripe-pale"></div>
    <div class="stripe stripe-footer">
      <span class="address">P.O. Box: 48210 · Dubai, United Arab Emirates</span>
      <span class="website">www.belsoravin.com</span>
    </div>
  </section>

  <section class="card card-back" aria-label="Business card back">
    <div class="back-top">
      <div class="brand-mark">
        <span class="brand-square"></span>
        <span class="brand-name">BEL SORAVIN GROUP</span>
      </div>
    </div>
    <div class="back-body">
      <div class="person">
        <p class="person-name">Korvan EL Mistrani</p>
        <p class="person-role">operation manager</p>
      </div>
      <ul class="contact-list">
        <li>P.: +100 555 0142</li>
        <li>M.: +100 555 0142</li>
        <li>F.: +100 555 0142</li>
        <li>E.: info@belsoravin.com</li>
      </ul>
    </div>
    <div class="back-edge"></div>
    <div class="back-footer silver-band">
      <p class="address">P.O. Box: 48210<br>Dubai, United Arab Emirates</p>
      <p class="website">www.belsoravin.com</p>
    </div>
  </section>

</body>
</html>
```